Powerpoint template for company specialized in training and coaching

We are a company specialized in training and transforming Leaders of companies in their leadership skills. We also help companies transform their company culture. We look at what is positive and already works for the company. We need a powerpoint template for out training. The look and feel should be professional, warm and personal. We just launched our new website www.bridgeofcandor.nl so you can get a good feel. please also check our social media posts. Usually the diagonal stripes of our logo (the house) comes back here. https://www.linkedin.com/school/81920564/admin/feed/posts/
We need two template. One in our business colors https://bridgeofcandor.nl/zakelijk/ and one in our educational colors. https://bridgeofcandor.nl/opleidingen/.

```html
<!DOCTYPE html>
<html lang="nl">
<head>
<meta charset="utf-8">
<title>Bridge of Candor – presentatiesjabloon</title>
<link href="https://fonts.googleapis.com/css2?family=Poppins:wght@400;500;600;700&family=Questrial&display=swap" rel="stylesheet">
<style>
  :root{
    --teal:#3e6168;
    --teal-soft:#5f7f84;
    --mist:#d4dddd;
    --gold:#e4ac44;
    --gold-text:#e6ae4c;
    --copper:#b5683a;
    --ink:#1f2426;
    --black:#0d0d0d;
    --paper:#ffffff;
    --stage:#c8c8c8;
  }
  *{box-sizing:border-box;margin:0;padding:0}
  html,body{width:1200px;height:727px;overflow:hidden;background:var(--stage)}
  body{position:relative;font-family:"Questrial",sans-serif;color:var(--ink)}
  .slide{position:absolute;width:354px;height:199px;background:var(--paper);overflow:hidden}
  .c1{left:49px}.c2{left:419px}.c3{left:792px}
  .r1{top:49px}.r2{top:264px}.r3{top:477px}
  .abs{position:absolute}
  .photo{position:absolute}
  .brand{position:absolute;top:13px;right:18px;display:flex;align-items:center;gap:3px}
  .brand-mark{width:9px;height:9px;background:var(--teal)}
  .brand-name{font-family:"Poppins",sans-serif;font-weight:600;font-size:6.5px;line-height:6.5px;color:var(--teal)}
  .page-no{position:absolute;right:18px;bottom:10px;font-family:"Poppins",sans-serif;font-weight:600;font-size:8px}
  .h-bold{font-family:"Poppins",sans-serif;font-weight:600;color:var(--teal);line-height:1;white-space:nowrap}
  .h-light{font-family:"Questrial",sans-serif;font-weight:400;color:var(--ink);line-height:1;white-space:nowrap}

  /* cover */
  .cover-title{left:24px;top:156px;color:#fff;font-family:"Poppins",sans-serif;font-weight:600;font-size:12.2px;line-height:17px}
  .cover-badge{left:0;top:4px;width:110px;height:36px;background:#fff;border-radius:0 18px 18px 0}
  .cover-badge .brand{left:24px;top:12px;right:auto}

  /* quote */
  .quote{left:152px;top:44px;font-size:11.2px;line-height:16.2px;color:var(--gold-text);text-transform:uppercase}
  .quote strong{font-family:"Poppins",sans-serif;font-weight:600;color:var(--teal);font-size:10.6px}
  .pill{left:235px;top:161px;width:74px;height:18px;border-radius:9px;background:var(--teal);color:#fff;font-family:"Poppins",sans-serif;font-weight:500;font-size:7.5px;display:flex;align-items:center;justify-content:center}

  /* opleidingen */
  .intro-list{left:233px;top:73px;width:110px;font-size:5.8px;line-height:10.3px}
  .chev{left:220px;top:73px;width:8px;height:8px;background:var(--teal)}

  /* team */
  .lead-copy{left:108px;top:51px;font-family:"Poppins",sans-serif;font-weight:600;font-size:4.9px;line-height:6.4px}
  .coach{position:absolute;top:88px;width:70px;height:86px;background:#fff;border-radius:4px;box-shadow:0 1px 3px rgba(0,0,0,.08)}
  .coach svg{position:absolute;left:3px;top:-5px}
  .coach-name{position:absolute;bottom:8px;width:100%;text-align:center;font-family:"Poppins",sans-serif;font-weight:500;font-size:5.2px}

  /* workshop */
  .course{position:absolute;top:90px;width:100px;height:95px;background:var(--mist);border-radius:7px;padding:29px 9px 0}
  .course.is-featured{background:var(--teal);color:#fff}
  .course-photo{position:absolute;top:64px;width:82px;height:53px}
  .course-name{font-family:"Poppins",sans-serif;font-weight:600;font-size:4.6px;line-height:6px;color:var(--teal);margin-bottom:5px}
  .course.is-featured .course-name{color:#fff}
  .course-copy{font-size:4.1px;line-height:5px}

  /* agenda */
  .date{position:absolute;left:135px;width:44px;height:39px;display:flex;flex-direction:column;align-items:center;justify-content:center;font-family:"Poppins",sans-serif}
  .date b{font-weight:400;font-size:14px;line-height:14px}
  .date span{font-size:4.4px;margin-top:2px}
  .date.soft{background:var(--mist);color:var(--teal)}
  .date.teal{background:var(--teal);color:#fff}
  .date.black{background:var(--black);color:#fff}
  .event{position:absolute;left:200px;width:120px}
  .event h4{font-family:"Poppins",sans-serif;font-weight:500;font-size:5px;color:var(--teal);margin-bottom:3px}
  .event h4.faint{color:#c2cccc}
  .event p{font-size:4.2px;line-height:5.2px}

  /* reviews */
  .review{position:absolute;top:72px;width:93px;height:110px;background:var(--mist)}
  .review-name{position:absolute;top:9px;left:29px;font-size:7.4px;white-space:nowrap}
  .review-role{position:absolute;top:21px;left:29px;font-size:5.8px;font-style:italic;white-space:nowrap}
  .review-text{position:absolute;top:40px;left:6px;width:80px;font-size:5.6px;line-height:6.7px}
  .stars{position:absolute;bottom:11px;left:7px;color:var(--copper);font-size:7px;letter-spacing:1px}

  /* contact */
  .contact-label{font-family:"Poppins",sans-serif;font-weight:600;font-size:6.3px}
  .contact-value{font-size:6.3px;color:var(--gold-text)}
</style>
</head>
<body>

<!-- 1 cover -->
<section class="slide c1 r1">
  <div class="photo" role="img" aria-label="Groepstraining: trainer bij flip-over voor deelnemers in een kring" style="left:0;top:0;width:297px;height:199px;background:linear-gradient(135deg,#6e6558 0%,#9a8f80 40%,#4f4a42 100%)"></div>
  <svg class="abs" style="left:297px;top:0" width="57" height="199" viewBox="0 0 57 199">
    <polygon points="0,0 2,0 26,17 0,38" fill="var(--teal)"/>
    <polygon points="0,100 57,40 57,78 0,138" fill="var(--black)"/>
    <polygon points="0,175 57,110 57,155 20,199 0,199" fill="var(--teal)"/>
  </svg>
  <div class="abs cover-badge"><div class="brand"><span class="brand-mark"></span><span class="brand-name">Bridge<br>of Candor</span></div></div>
  <div class="abs cover-title">LEADERSHIP TRAINING AND<br>TRANSFORMATION IN LEADERSHIP SKILLS</div>
</section>

<!-- 2 quote -->
<section class="slide c2 r1">
  <div class="photo" role="img" aria-label="Portret van een coach in een industriële ruimte" style="left:2px;top:2px;width:131px;height:197px;background:linear-gradient(180deg,#5b4e44,#8a7a6c 50%,#3d3631)"></div>
  <div class="brand"><span class="brand-mark"></span><span class="brand-name">Bridge<br>of Candor</span></div>
  <p class="abs quote">Before being a leader,<br>success is about maturing<br>and developing yourself.<br><strong>When you're a leader,</strong><br>success is about maturing<br>and developing others.</p>
  <div class="abs pill">HAROLD BRINK</div>
  <div class="page-no">2</div>
</section>

<!-- 3 opleidingen -->
<section class="slide c3 r1">
  <svg class="abs" style="left:150px;top:34px" width="70" height="110" viewBox="0 0 70 110">
    <path d="M10,25 C20,0 60,-5 68,25 L68,110 L40,110 C20,95 45,70 30,50 C15,35 5,38 10,25Z" fill="var(--gold)"/>
    <path d="M10,25 C20,0 60,-5 68,25 L68,20 C50,5 25,5 10,25Z" fill="var(--copper)" opacity=".6"/>
  </svg>
  <h2 class="abs h-bold" style="left:16px;top:20px;font-size:22.5px">Opleidingen</h2>
  <div class="brand"><span class="brand-mark"></span><span class="brand-name">Bridge<br>of Candor</span></div>
  <div class="photo" role="img" aria-label="Trainer wijst naar flip-over met gele memobriefjes" style="left:0;top:55px;width:211px;height:144px;background:linear-gradient(135deg,#a89a86,#6c5d4d 60%,#4a3f36)"></div>
  <svg class="abs chev" viewBox="0 0 8 8"><path d="M3,2 L5,4 L3,6" stroke="#fff" stroke-width="1" fill="none"/></svg>
  <p class="abs intro-list">Wil jij ook coach worden, teams begeleiden of met organisatieverandering aan de slag?<br>Geef je professionele ontwikkeling een boost met een erkende post-hbo opleiding of met een praktische en compacte opleiding.</p>
  <div class="page-no">3</div>
</section>

<!-- 4 coaches -->
<section class="slide c1 r2">
  <h2 class="abs h-bold" style="left:24px;top:20px;font-size:22px">Zij helpen je</h2>
  <h2 class="abs h-light" style="left:24px;top:43px;font-size:22px">verder</h2>
  <div class="brand"><span class="brand-mark"></span><span class="brand-name">Bridge<br>of Candor</span></div>
  <p class="abs lead-copy">Als jij je echt verder wil ontwikkelen, als je echt wil groeien,<br>heb je een coach nodig die zijn of haar vak tot in de finesses verstaat.<br>Met minder neem je geen genoegen. Maak kennis met onze bevlogen experts.</p>
  <div class="coach" style="left:20px"><svg width="64" height="66" viewBox="0 0 64 66" role="img" aria-label="Portretfoto coach"><path d="M12,14 C20,0 40,4 52,12 C66,20 62,40 54,50 C44,64 20,66 8,54 C-2,42 4,26 12,14Z" fill="#8ea4a6"/><rect x="8" y="24" width="48" height="42" rx="18" fill="#3f4a58"/></svg><div class="coach-name">Joost Verbeek</div></div>
  <div class="coach" style="left:101px"><svg width="64" height="66" viewBox="0 0 64 66" role="img" aria-label="Portretfoto coach"><path d="M14,8 C26,-2 50,4 56,18 C64,34 60,54 46,62 C30,70 8,60 4,44 C0,30 4,16 14,8Z" fill="#c69a7c"/><rect x="8" y="24" width="48" height="42" rx="18" fill="#3d8a8a"/></svg><div class="coach-name">Ilse Koopman</div></div>
  <div class="coach" style="left:182px"><svg width="64" height="66" viewBox="0 0 64 66" role="img" aria-label="Portretfoto coach"><path d="M18,6 C32,-4 52,8 58,24 C64,42 56,60 40,64 C22,68 6,56 4,40 C2,26 8,14 18,6Z" fill="#a06b86"/><rect x="8" y="24" width="48" height="42" rx="18" fill="#2c3442"/></svg><div class="coach-name">Bart Wessels</div></div>
  <div class="coach" style="left:263px"><svg width="64" height="66" viewBox="0 0 64 66" role="img" aria-label="Portretfoto coach"><path d="M10,18 C18,2 42,-2 56,10 C66,22 62,44 52,56 C40,68 18,66 8,54 C0,42 4,28 10,18Z" fill="var(--gold)"/><rect x="8" y="24" width="48" height="42" rx="18" fill="#33406a"/></svg><div class="coach-name">Renate Dijkstra</div></div>
  <div class="page-no">4</div>
</section>

<!-- 5 workshop -->
<section class="slide c2 r2">
  <h2 class="abs h-bold" style="left:17px;top:13px;font-size:22px">opleiding tot</h2>
  <h2 class="abs h-light" style="left:17px;top:35px;font-size:22px">praktische workshop</h2>
  <div class="brand"><span class="brand-mark"></span><span class="brand-name">Bridge<br>of Candor</span></div>
  <div class="course" style="left:17px"><div class="course-name">Leergang Ontwikkeling<br>Mens en Organisatie</div><p class="course-copy">Bij de erkende post-hbo opleiding leer je de basis van coaching. Je volgt modules in je eigen tempo en bepaalt zelf de verdieping.</p></div>
  <div class="course is-featured" style="left:127px"><div class="course-name">Coaching<br>skills</div><p class="course-copy">In twee dagen leer je de grondbeginselen van het coachen. Hoe breng je iemand in beweging en hoe zet je jouw impact in?</p></div>
  <div class="course" style="left:237px"><div class="course-name">Succesvolle teams<br>met Verhoef</div><p class="course-copy">Wil je teams naar nieuwe hoogten brengen? In deze eendaagse workshop leer je praktische tools om samenwerking effectief te verbeteren.</p></div>
  <div class="course-photo" role="img" aria-label="Vrouw werkt aan laptop in lichte keuken" style="left:26px;background:linear-gradient(135deg,#e8e1d8,#bfae9c)"></div>
  <div class="course-photo" role="img" aria-label="Coachgesprek tussen twee personen" style="left:136px;background:linear-gradient(135deg,#c9c0b4,#3f5568)"></div>
  <div class="course-photo" role="img" aria-label="Team overlegt rond een tafel" style="left:246px;background:linear-gradient(135deg,#ddd6cc,#6e7f8c)"></div>
  <div class="page-no">5</div>
</section>

<!-- 6 agenda -->
<section class="slide c3 r2">
  <div class="brand"><span class="brand-mark"></span><span class="brand-name">Bridge<br>of Candor</span></div>
  <h2 class="abs h-bold" style="left:24px;top:52px;font-size:22px">2024</h2>
  <h2 class="abs h-light" style="left:24px;top:76px;font-size:22px;line-height:23px">TRAINEE<br>AGENDA</h2>
  <div class="date soft" style="top:50px"><b>17</b><span>OCTOBER</span></div>
  <div class="date teal" style="top:94px"><b>25</b><span>NOVEMBER</span></div>
  <div class="date black" style="top:138px"><b>07</b><span>DECEMBER</span></div>
  <div class="event" style="top:57px"><h4 class="faint">DESCRIPTION TEXT HERE</h4><p>Lorem Ipsum is simply dummy text of the printing and typesetting industry. Lorem Ipsum has been the industry's standard dummy text</p></div>
  <div class="event" style="top:103px"><h4>DESCRIPTION TEXT HERE</h4><p>Lorem Ipsum is simply dummy text of the printing and typesetting industry. Lorem Ipsum has been the industry's standard dummy text</p></div>
  <div class="event" style="top:145px"><h4>DESCRIPTION TEXT HERE</h4><p>Lorem Ipsum is simply dummy text of the printing and typesetting industry. Lorem Ipsum has been the industry's standard dummy text</p></div>
</section>

<!-- 7 reviews -->
<section class="slide c1 r3">
  <h2 class="abs h-bold" style="left:17px;top:14px;font-size:22px">What our</h2>
  <h2 class="abs h-light" style="left:17px;top:36px;font-size:22px">Members say</h2>
  <div class="brand"><span class="brand-mark"></span><span class="brand-name">Bridge<br>of Candor</span></div>
  <div class="review" style="left:65px"><div class="review-name">Mila Hendriks</div><div class="review-role">Training Member</div><p class="review-text">"Lorem Ipsum is simply dummy text of the printing and typesetting industry. Lorem Ipsum has been the industry's standard dummy text ever since the 1500s"</p><div class="stars">★★★★★</div></div>
  <div class="review" style="left:212px"><div class="review-name">Tom Rijkers</div><div class="review-role">Training Member</div><p class="review-text">"Lorem Ipsum is simply dummy text of the printing and typesetting industry. Lorem Ipsum has been the industry's standard dummy text ever since the 1500s"</p><div class="stars">★★★★★</div></div>
  <svg class="abs" style="left:22px;top:58px" width="70" height="70" viewBox="0 0 70 70"><path d="M14,6 C26,-2 46,2 50,14 L50,50 C44,66 30,66 28,56 C26,46 12,50 6,40 C0,30 4,14 14,6Z" fill="var(--copper)"/><rect x="21" y="5" width="44" height="42" fill="var(--teal)"/></svg>
  <svg class="abs" style="left:170px;top:52px" width="70" height="70" viewBox="0 0 70 70"><path d="M6,14 C12,0 40,-2 50,8 C58,16 54,30 48,40 L14,40 C4,34 2,24 6,14Z" fill="var(--copper)"/><rect x="21" y="11" width="44" height="42" fill="var(--teal)"/></svg>
</section>

<!-- 8 break -->
<section class="slide c2 r3" style="background:var(--teal)">
  <svg class="abs" style="left:0;top:0" width="354" height="199" viewBox="0 0 354 199">
    <polygon points="0,140 110,0 190,0 20,199 0,199" fill="var(--teal-soft)" opacity=".55"/>
    <polygon points="150,199 280,40 300,70 200,199" fill="var(--teal-soft)" opacity=".5"/>
    <polygon points="230,199 354,70 354,125 290,199" fill="var(--black)"/>
    <defs><linearGradient id="breakBlob" x1="0" y1="0" x2="0" y2="1"><stop offset="0" stop-color="#e2ad47"/><stop offset="1" stop-color="#6f765a"/></linearGradient></defs>
    <path d="M150,18 C185,-8 235,12 233,60 C232,100 270,130 250,160 C225,195 170,175 135,165 C95,155 65,125 85,100 C105,75 120,40 150,18Z" fill="url(#breakBlob)"/>
  </svg>
  <div class="abs" style="left:122px;top:60px;color:#fff;font-family:'Poppins',sans-serif;font-weight:700;font-size:32px;line-height:32px">BREAK</div>
  <div class="abs" style="left:122px;top:93px;color:#fff;font-size:32px;line-height:34px">SLIDE</div>
  <div class="abs" style="left:165px;top:133px;color:#fff;font-size:14px">35 MINUTES</div>
</section>

<!-- 9 contact -->
<section class="slide c3 r3">
  <svg class="abs" style="left:0;top:0" width="354" height="199" viewBox="0 0 354 199">
    <polygon points="138,199 138,75 200,0 255,0 170,199" fill="var(--teal-soft)" opacity=".85"/>
    <polygon points="230,199 320,100 345,120 262,199" fill="var(--teal-soft)" opacity=".85"/>
    <polygon points="182,199 315,60 354,85 354,100 230,199" fill="var(--black)"/>
    <polygon points="320,150 354,120 354,160 330,180" fill="var(--teal-soft)"/>
    <defs><linearGradient id="thanksBlob" x1="0" y1="0" x2="1" y2="1"><stop offset="0" stop-color="#e2ad47"/><stop offset="1" stop-color="#4f6a68"/></linearGradient></defs>
    <path d="M190,30 C215,10 265,10 290,35 C320,65 335,110 305,145 C280,175 235,190 200,170 C165,150 150,115 165,85 C175,62 170,45 190,30Z" fill="url(#thanksBlob)"/>
    <path d="M240,20 C250,10 262,25 270,40 C258,36 245,32 240,20Z" fill="var(--copper)" opacity=".85"/>
    <path d="M150,135 C160,120 168,125 158,140 C154,146 148,142 150,135Z" fill="var(--copper)" opacity=".85"/>
  </svg>
  <div class="abs" style="left:195px;top:70px;color:#fff;font-family:'Poppins',sans-serif;font-weight:700;font-size:33px;line-height:33px;text-align:center;width:110px">Thank<br>You</div>
  <h2 class="abs h-bold" style="left:24px;top:46px;font-size:22px">GET IN</h2>
  <h2 class="abs h-light" style="left:24px;top:68px;font-size:22px">TOUCH</h2>
  <svg class="abs" style="left:25px;top:101px" width="22" height="20" viewBox="0 0 22 20"><path d="M0,8 L8,0 L16,8 L16,20 L0,20Z" fill="var(--gold)"/><rect x="8" y="9" width="12" height="8" fill="#fff" stroke="var(--ink)" stroke-width="1"/><path d="M8,9 L14,14 L20,9" stroke="var(--ink)" fill="none" stroke-width="1"/></svg>
  <div class="abs" style="left:57px;top:106px"><div class="contact-label">E-mailadres</div><div class="contact-value">hoi@bridgeofcandor.nl</div></div>
  <svg class="abs" style="left:25px;top:136px" width="22" height="20" viewBox="0 0 22 20"><path d="M0,8 L8,0 L16,8 L16,20 L0,20Z" fill="var(--gold)"/><path d="M9,8 C8,12 11,17 16,18 L18,16 L15,14 L13,15 C12,14 11,12 11,11 L12,10 L11,7Z" fill="#fff" stroke="var(--ink)" stroke-width=".8"/></svg>
  <div class="abs" style="left:58px;top:141px"><div class="contact-label">Telefoonnummer</div><div class="contact-value">085 0412786</div></div>
</section>

</body>
</html>
```